Poster design for a company operating care homes in the UK showcasing our core values

We need a poster to display in our care homes showcasing our new core values:

Purpose
We are driven by a clear understanding of why we do what we do: to enrich lives, honour legacies and make a meaningful difference every day, for our residents, their families, our colleagues and our community.

Excellence
We hold ourselves to the highest standards, delivering exceptional care and creating an environment where both residents and staff can thrive.

Openness
We build trust through honest, respectful communication, welcoming feedback, sharing ideas, and embracing change as a path to continuous growth.

Passion
We are passionate about delivering exceptional care. We take pride in what we do and in making a real difference in people’s lives.

Learning
We are committed to personal and professional growth; empowering each other through ongoing development, reflection, and shared knowledge.

Empathy
We actively listen and seek to understand before being understood, recognising the unique stories, feelings, and needs of others.

I have attached a small graphic that we would like you try to incorporate, in addition to our company logo. Please theme the rest of the poster around our company colours.

```html
<!DOCTYPE html>
<html lang="en">
<head>
<meta charset="utf-8">
<title>Our Core Values – Halvern</title>
<link href="https://fonts.googleapis.com/css2?family=Anton&family=Inter:wght@400;500;700&family=Open+Sans:wght@400;600;700&display=swap" rel="stylesheet">
<style>
  :root {
    --navy: #3b5571;
    --peach: #f1a68a;
    --peach-text: #b4583a;
    --ring: #f0b193;
    --paper: #f4f5f7;
  }
  html, body {
    margin: 0;
    padding: 0;
    width: 848px;
    height: 1200px;
    overflow: hidden;
    background: var(--paper);
  }
  .poster {
    position: relative;
    width: 842px;
    height: 1191px;
    transform: scale(1.0071);
    transform-origin: 0 0;
    background: var(--paper);
    font-family: "Inter", Arial, sans-serif;
  }
  .value-wheel {
    position: absolute;
    inset: 0;
    width: 842px;
    height: 1191px;
  }
  .brand {
    position: absolute;
    left: 46px;
    top: 50px;
    display: flex;
    align-items: center;
    gap: 14px;
    font-family: "Open Sans", Arial, sans-serif;
    font-weight: 700;
    font-size: 42px;
    letter-spacing: 1px;
    color: var(--navy);
  }
  .brand-mark {
    width: 40px;
    height: 40px;
    background: var(--peach);
  }
  .wheel-title {
    position: absolute;
    left: 0;
    width: 842px;
    top: 612px;
    margin: 0;
    text-align: center;
    font-family: "Anton", Impact, sans-serif;
    font-weight: 400;
    font-size: 43px;
    line-height: 1;
    color: var(--navy);
  }
  .value {
    position: absolute;
  }
  .value h2 {
    margin: 0;
    font-family: "Anton", Impact, sans-serif;
    font-weight: 400;
    font-size: 36px;
    line-height: 1.1;
  }
  .value p {
    margin: 9px 0 0;
    font-size: 10.3px;
    line-height: 1.3;
    letter-spacing: -0.1px;
  }
  .value--navy h2 { color: var(--navy); }
  .value--navy p { color: var(--peach-text); }
  .value--peach h2 { color: var(--peach); }
  .value--peach p { color: var(--navy); }

  .bracket {
    position: absolute;
    border-color: var(--peach);
    border-style: solid;
    border-width: 0;
  }
  .bracket--top { border-left-width: 1px; border-top-width: 1px; }
  .bracket--bottom { border-left-width: 1px; border-bottom-width: 1px; }
  .bracket--line { border-left-width: 1px; }

  .value--excellence { left: 370px; top: 176px; width: 175px; }
  .value--openness { left: 610px; top: 228px; width: 178px; }
  .value--purpose { left: 72px; top: 256px; width: 192px; }
  .value--empathy { left: 63px; top: 862px; width: 185px; }
  .value--passion { left: 610px; top: 862px; width: 180px; }
  .value--learning { left: 370px; top: 994px; width: 180px; }
</style>
</head>
<body>
<main class="poster">
  <svg class="value-wheel" viewBox="0 0 842 1191" aria-hidden="true">
    <defs>
      <linearGradient id="navy-fill" x1="0" y1="0" x2="0" y2="1">
        <stop offset="0" stop-color="#39526f"/>
        <stop offset="1" stop-color="#4f6b7a"/>
      </linearGradient>
      <linearGradient id="peach-fill" x1="0" y1="0" x2="0" y2="1">
        <stop offset="0" stop-color="#f2a68b"/>
        <stop offset="1" stop-color="#f0ad8e"/>
      </linearGradient>
      <filter id="tile-shadow" x="-20%" y="-20%" width="140%" height="140%">
        <feDropShadow dx="0" dy="2" stdDeviation="3" flood-color="#1f2d3d" flood-opacity="0.25"/>
      </filter>
      <polygon id="hex-tile" points="0,-87 75,-43.5 75,43.5 0,87 -75,43.5 -75,-43.5" stroke-width="20" stroke-linejoin="round"/>
    </defs>

    <circle cx="421" cy="625" r="235" fill="none" stroke="var(--ring)" stroke-width="3"/>

    <g filter="url(#tile-shadow)">
      <use href="#hex-tile" x="421" y="394" fill="url(#navy-fill)" stroke="url(#navy-fill)"/>
      <use href="#hex-tile" x="622" y="505" fill="url(#peach-fill)" stroke="url(#peach-fill)"/>
      <use href="#hex-tile" x="622" y="742" fill="url(#navy-fill)" stroke="url(#navy-fill)"/>
      <use href="#hex-tile" x="421" y="858" fill="url(#peach-fill)" stroke="url(#peach-fill)"/>
      <use href="#hex-tile" x="220" y="752" fill="url(#navy-fill)" stroke="url(#navy-fill)"/>
      <use href="#hex-tile" x="220" y="505" fill="url(#peach-fill)" stroke="url(#peach-fill)"/>
    </g>

    <g font-family="'Open Sans', Arial, sans-serif" font-weight="700" font-size="64" text-anchor="middle">
      <text x="421" y="417" fill="var(--peach)">E</text>
      <text x="622" y="528" fill="var(--navy)">O</text>
      <text x="622" y="765" fill="var(--peach)">P</text>
      <text x="421" y="881" fill="var(--navy)">L</text>
      <text x="220" y="775" fill="var(--peach)">E</text>
      <text x="220" y="528" fill="var(--navy)">P</text>
    </g>
  </svg>

  <div class="brand">
    <span class="brand-mark"></span>
    <span class="brand-name">HALVERN</span>
  </div>

  <span class="bracket bracket--top" style="left:355px; top:168px; width:22px; height:132px;"></span>
  <span class="bracket bracket--line" style="left:596px; top:262px; height:128px;"></span>
  <span class="bracket bracket--bottom" style="left:56px; top:275px; width:22px; height:191px;"></span>
  <span class="bracket bracket--top" style="left:48px; top:782px; width:22px; height:193px;"></span>
  <span class="bracket bracket--line" style="left:596px; top:864px; height:136px;"></span>
  <span class="bracket bracket--bottom" style="left:355px; top:960px; width:22px; height:165px;"></span>

  <h1 class="wheel-title">Our Core Values</h1>

  <section class="value value--peach value--excellence">
    <h2>Excellence</h2>
    <p>We hold ourselves to the highest standards, delivering exceptional care and creating an environment where both residents and staff can thrive</p>
  </section>

  <section class="value value--navy value--openness">
    <h2>Openness</h2>
    <p>We build trust through honest, respectful communication, welcoming feedback, sharing ideas, and embracing change as a path to continuous growth</p>
  </section>

  <section class="value value--navy value--purpose">
    <h2>Purpose</h2>
    <p>We are driven by a clear understanding of why we do what we do: to enrich lives, honour legacies and make a meaningful difference every day, for our residents, their families, our colleagues and our community</p>
  </section>

  <section class="value value--peach value--empathy">
    <h2>Empathy</h2>
    <p>We actively listen and seek to understand before being understood, recognising the unique stories, feelings, and needs of others</p>
  </section>

  <section class="value value--peach value--passion">
    <h2>Passion</h2>
    <p>We are passionate about delivering exceptional care. We take pride in what we do and in making a real difference in people’s lives</p>
  </section>

  <section class="value value--navy value--learning">
    <h2>Learning</h2>
    <p>We are committed to personal and professional growth; empowering each other through ongoing development, reflection, and shared knowledge</p>
  </section>
</main>
</body>
</html>
```